Book cover for a book about time management for women

We need a book cover for a book about time management for women written by a woman. Even though the book has a provocative title "Calendar rebellion" based on the seminars the author holds for women seeking the change in their life, it has nothing to do with the words themselves. The subtitle is "Steer each day by choice. An opening guide on hour mastery among ladies"

Preferred fonts (not necessarily):
Plus Jakarta Sans
Tiempos Headline

Preferred colours (not necessarily):
- orange
- pastel "highlighters"

We look for a simple/clean design that catches the attention of the women without too many graphic elements.

Target Market(s)

Women that want to change and organise their life

Industry/Entity Type

productivity, marketing, work-life balance

Font styles to use
Other font styles liked:
• Plus Jakarta Sans, Tiempos Headline

Colors
F0912C
F2A743
F7CA91
FBE8D2
FDF5EE
A7469A
B969AE
D3A5CF
EDDBEB
F8F0F9

Requirements
Must have
• Famine feeling as the target audience are women with drive to better life
Should not have
• No explicit images or sexually motivated themes

```html
<!DOCTYPE html>
<html lang="en">
<head>
<meta charset="utf-8">
<title>Calendar rebellion — wraparound cover</title>
<link rel="stylesheet" href="https://fonts.googleapis.com/css2?family=Plus+Jakarta+Sans:ital,wght@0,500;0,600;1,500&family=Source+Serif+4:opsz,wght@8..60,500;8..60,800&family=Tinos&display=swap">
<style>
  :root{
    --page:#ffffff;
    --cream:#fbe8d2;
    --blush:#f8d8e4;
    --orchid-light:#f6c8ec;
    --band-top:#b969ae;
    --band-bottom:#9b4d92;
    --plum:#a7469a;
    --lilac:#d3a5cf;
    --orange:#f0912c;
    --ink:#111111;
    --white:#ffffff;
    --dial:#eeeae4;
  }
  *{margin:0;padding:0;box-sizing:border-box}
  html,body{width:1200px;height:1200px;overflow:hidden;background:var(--page)}
  .wrap-cover{
    position:absolute;left:0;top:192px;width:1200px;height:815px;
    background:linear-gradient(180deg,var(--cream) 0%,var(--blush) 55%,var(--orchid-light) 100%);
    overflow:hidden;
  }
  .band-top{position:absolute;left:0;top:0;width:100%;height:27px;background:var(--band-top)}
  .band-bottom{position:absolute;left:0;bottom:0;width:100%;height:50px;background:var(--band-bottom)}

  /* back */
  .back-clock{position:absolute;left:231px;top:43px;width:94px;height:94px}
  .back-copy{
    position:absolute;left:70px;top:182px;width:415px;
    font-family:"Tinos",serif;font-size:14.2px;line-height:18.8px;color:var(--ink);
    text-align:justify;hyphens:auto;
  }
  .back-copy p+p{margin-top:18px}
  .code-box{position:absolute;left:327px;top:673px;width:158px;height:83px;background:var(--white)}

  /* spine */
  .spine{
    position:absolute;left:558px;top:0;width:81px;height:765px;
  }
  .spine-text{
    position:absolute;left:62px;top:40px;transform-origin:0 0;transform:rotate(90deg);
    white-space:nowrap;display:flex;align-items:baseline;width:700px;color:var(--ink);
  }
  .spine-title{font-family:"Source Serif 4",serif;font-size:34px;font-weight:500;letter-spacing:-0.5px}
  .spine-title b{font-weight:800;letter-spacing:2px;margin-left:10px}
  .spine-author{font-family:"Plus Jakarta Sans",sans-serif;font-size:25px;font-weight:500;margin-left:auto}

  /* front */
  .front{position:absolute;left:639px;top:0;width:561px;height:815px}
  .tagline{
    position:absolute;right:28px;top:2px;height:27px;line-height:27px;
    font-family:"Plus Jakarta Sans",sans-serif;font-style:italic;font-weight:500;
    font-size:17.5px;color:var(--white);white-space:nowrap;
  }
  .title{position:absolute;left:0;top:48px;width:561px;text-align:center;color:var(--ink);font-family:"Source Serif 4",serif}
  .title-small{display:block;font-size:46px;font-weight:500;line-height:48px;letter-spacing:-0.5px}
  .title-large{display:block;font-size:58px;font-weight:800;line-height:76px;letter-spacing:3px}
  .subtitle{
    position:absolute;left:0;top:196px;width:561px;text-align:center;
    font-family:"Plus Jakarta Sans",sans-serif;font-weight:500;font-size:22.5px;color:var(--ink);
  }
  .hero-art{
    position:absolute;left:112px;top:245px;width:318px;height:518px;border-radius:160px 160px 150px 150px;
    background:radial-gradient(ellipse at 50% 55%,rgba(240,145,44,.55) 0%,rgba(240,145,44,.25) 35%,rgba(185,105,174,.25) 70%,rgba(185,105,174,0) 100%);
  }
  .author{
    position:absolute;left:0;bottom:0;width:561px;height:50px;line-height:50px;text-align:center;
    font-family:"Plus Jakarta Sans",sans-serif;font-weight:600;font-size:25px;color:var(--white);
  }
</style>
</head>
<body>
<main class="wrap-cover">
  <div class="band-top"></div>
  <div class="band-bottom"></div>

  <section class="back">
    <svg class="back-clock" viewBox="0 0 94 94" aria-hidden="true">
      <circle cx="47" cy="47" r="43" fill="var(--dial)" stroke="var(--band-top)" stroke-width="6"/>
      <line x1="47" y1="47" x2="34" y2="42" stroke="var(--ink)" stroke-width="2.5" stroke-linecap="round"/>
      <line x1="47" y1="47" x2="66" y2="37" stroke="var(--ink)" stroke-width="1.5" stroke-linecap="round"/>
      <circle cx="47" cy="47" r="3" fill="var(--ink)"/>
    </svg>
    <div class="back-copy">
      <p>Lorem ipsum dolor sit amet, consectetur adipiscing elit, sed do eiusmod tempor incididunt ut labore et dolore magna aliqua. Quis ipsum suspendisse ultrices gravida. Risus commodo viverra maecenas accumsan lacus vel facilisis. Lorem ipsum dolor sit amet, consectetur adipiscing elit, sed do eiusmod tempor incididunt ut labore et dolore magna aliqua. Quis ipsum suspendisse ultrices gravida. Risus commodo viverra maecenas accumsan lacus vel facilisis.</p>
      <p>Lorem ipsum dolor sit amet, consectetur adipiscing elit, sed do eiusmod tempor incididunt ut labore et dolore magna aliqua. Quis ipsum suspendisse ultrices gravida. Risus commodo viverra maecenas accumsan lacus vel facilisis. Lorem ipsum dolor sit amet, consectetur adipiscing elit, sed do eiusmod tempor incididunt ut labore et dolore magna aliqua. Quis ipsum suspendisse ultrices gravida. Risus commodo viverra maecenas accumsan lacus vel facilisis. Lorem ipsum dolor sit amet, consectetur adipiscing elit, sed do eiusmod tempor incididunt ut labore et dolore magna aliqua. Quis ipsum suspendisse ultrices gravida. Risus commodo viverra maecenas accumsan lacus vel facilisis.</p>
    </div>
    <div class="code-box"></div>
  </section>

  <section class="spine">
    <div class="spine-text">
      <span class="spine-title">Calendar<b>REBELLION</b></span>
      <span class="spine-author">Author Name</span>
    </div>
  </section>

  <section class="front">
    <p class="tagline">An opening guide on hour mastery among ladies</p>
    <h1 class="title">
      <span class="title-small">Calendar</span>
      <span class="title-large">REBELLION</span>
    </h1>
    <p class="subtitle">Steer each day by choice</p>
    <div class="hero-art" role="img" aria-label="Illustration of a woman in an orange dress riding a clock unicycle while juggling purple icons for goals, family, cooking, mail and love"></div>
    <p class="author">Author Name</p>
  </section>
</main>
</body>
</html>
```